Construction machinery rental / heavy equipment rental needs a nice billboard

We need a billboard for our company.
We rent out construction machinery such as excavators, wheel loaders, wheel dumpers and so on...

I would like an elegant, simple, dark design.
Colors: black yellow grey white

The following must be on the billboard:
Logo
phone number: 078 / 513 90 41
website: www.kiesgrube-talwerk.ch
the machines I rent out: Bagger bis 10T, Radlader, Dumper, Raupenkipper

the font in the logo is: Square 721

Final format 2950 x 1900mm
I have uploaded pictures:
"Excavator 1-6" are my pictures, which can be used
"Sample 1-4" are pictures whose style I like
"Billboard" are billboards which I like

Requirements
Must have
• The following must be on the billboard: Logo phone number: 078 / 513 90 41 website: www.kiesgrube-talwerk.ch the machines I rent out: Bagger bis 10T, Radlader, Dumper, Raupenkipper

```html
<!DOCTYPE html>
<html lang="de">
<head>
<meta charset="utf-8">
<title>Talwerk – Billboard</title>
<link rel="stylesheet" href="https://fonts.googleapis.com/css2?family=Saira:ital,wght@0,700;0,800;1,800;1,900&display=swap">
<style>
  :root {
    --page: #d9d9d9;
    --board: #000000;
    --photo-core: #3d3d3d;
    --photo-mid: #262626;
    --photo-edge: #141414;
    --silver-hi: #ffffff;
    --silver-lo: #9a9a9a;
    --gold: #d4bc3a;
    --grey-text: #d6d6d6;
  }
  html, body {
    margin: 0;
    width: 1200px;
    height: 1200px;
    overflow: hidden;
    background: var(--page);
  }
  .billboard {
    position: absolute;
    left: 0;
    top: 213px;
    width: 1200px;
    height: 773px;
    background: var(--board);
    overflow: hidden;
    font-family: "Saira", sans-serif;
  }
  .backdrop-photo {
    position: absolute;
    left: 0; top: 0;
    width: 720px; height: 773px;
    background: radial-gradient(ellipse 60% 55% at 40% 45%, #1c1c1c 0%, #101010 60%, var(--board) 100%);
  }
  .machine-photo {
    position: absolute;
    left: 586px; top: 3px;
    width: 614px; height: 598px;
    background:
      radial-gradient(ellipse 55% 60% at 68% 58%, var(--photo-core) 0%, var(--photo-mid) 45%, var(--photo-edge) 75%, rgba(0,0,0,0) 100%);
  }
  .machine {
    position: absolute;
    left: 0; width: 722px;
    text-align: center;
  }
  .machine-name {
    display: block;
    font-weight: 900;
    font-style: italic;
    font-size: 66px;
    line-height: 1;
    letter-spacing: 1px;
    background: linear-gradient(180deg, var(--silver-hi) 20%, var(--silver-lo) 100%);
    -webkit-background-clip: text;
    background-clip: text;
    color: transparent;
    filter: drop-shadow(2px 3px 2px rgba(0,0,0,0.9));
  }
  .machine-rule {
    position: absolute;
    height: 4px;
    border-radius: 2px;
    background: linear-gradient(90deg, rgba(212,188,58,0) 0%, var(--gold) 25%, var(--gold) 75%, rgba(212,188,58,0) 100%);
  }
  .brand {
    position: absolute;
    left: 100px; top: 654px;
    display: flex;
    align-items: center;
    gap: 16px;
  }
  .brand-mark {
    width: 38px; height: 38px;
    background: var(--gold);
  }
  .brand-name {
    font-weight: 800;
    font-size: 64px;
    line-height: 1;
    color: var(--gold);
    letter-spacing: 2px;
  }
  .contact {
    position: absolute;
    left: 600px; top: 630px;
    width: 580px;
  }
  .phone {
    display: flex;
    align-items: center;
    gap: 12px;
  }
  .phone-icon { width: 38px; height: 44px; }
  .phone-number {
    font-weight: 900;
    font-style: italic;
    font-size: 64px;
    line-height: 1;
    color: var(--gold);
    letter-spacing: 2px;
  }
  .website {
    margin-top: 10px;
    font-weight: 800;
    font-size: 30px;
    line-height: 1;
    color: var(--grey-text);
    letter-spacing: 0.5px;
  }
</style>
</head>
<body>
  <main class="billboard">
    <div class="backdrop-photo" role="img" aria-label="Gedämpftes Foto eines Baggers im Hintergrund"></div>
    <div class="machine-photo" role="img" aria-label="Foto eines schwarzen Minibaggers mit Tieflöffel"></div>

    <section class="machine-list">
      <div class="machine" style="top:136px"><span class="machine-name">BAGGER BIS 10T</span></div>
      <div class="machine-rule" style="left:105px; width:530px; top:193px"></div>

      <div class="machine" style="top:227px"><span class="machine-name">RADLADER</span></div>
      <div class="machine-rule" style="left:146px; width:446px; top:284px"></div>

      <div class="machine" style="top:318px"><span class="machine-name">DUMPER</span></div>
      <div class="machine-rule" style="left:146px; width:446px; top:375px"></div>

      <div class="machine" style="top:411px"><span class="machine-name">RAUPENKIPPER</span></div>
      <div class="machine-rule" style="left:72px; width:592px; top:470px"></div>
    </section>

    <div class="brand">
      <span class="brand-mark"></span>
      <span class="brand-name">TALWERK</span>
    </div>

    <div class="contact">
      <div class="phone">
        <svg class="phone-icon" viewBox="0 0 38 44" aria-hidden="true">
          <path d="M9 4 L15 12 L11 17 Q14 26 21 31 L26 27 L33 34 L28 40 Q14 38 6 22 Q3 12 9 4 Z" fill="none" stroke="#d6d6d6" stroke-width="3.5" stroke-linejoin="round"/>
          <path d="M22 8 Q30 10 32 18" fill="none" stroke="#d6d6d6" stroke-width="3" stroke-linecap="round"/>
          <path d="M22 2 Q36 5 38 20" fill="none" stroke="#d6d6d6" stroke-width="3" stroke-linecap="round"/>
        </svg>
        <span class="phone-number">078 / 513 90 41</span>
      </div>
      <div class="website">www.kiesgrube-talwerk.ch</div>
    </div>
  </main>
</body>
</html>
```